Re-Design Korbalex.com make it more professional looking

We want to re-design this website, we are currently not happy with existing design. Some of the design examples are listed below.

https://trelvan.com/
https://www.quostel.com/
https://www.namity.com/projects/
https://www.flarnside.com/

The content on the website is final, there will be no change in the content. We just need to re-design the site. Features page on the site is very important and need to be layout very well.

Industry/Entity Type

It Professional

Number of Pages Required

4 page

Font styles to use
Sans Serif

Requirements
Must have
• Professional look and design like the examples i quoted above and a nice color theme. I do not have preferences but i like the quostel.com and trelvan.com

```html
<!DOCTYPE html>
<html lang="en">
<head>
<meta charset="utf-8">
<title>Korbalex – Project Management for Digital Agencies</title>
<link href="https://fonts.googleapis.com/css2?family=Montserrat:wght@400;600;700&family=Open+Sans:wght@400;600;700&display=swap" rel="stylesheet">
<style>
:root{
  --green:#7cb342;--green-band:#7dc052;--orange:#f7941d;--blue:#2ea3e3;--yellow:#f2c311;
  --dark:#2b2b2b;--text:#555;--muted:#888;--white:#fff;--light:#f4f4f4;--footer:#fafafa;
}
*{margin:0;padding:0;box-sizing:border-box}
html,body{width:1200px;height:3982px;overflow:hidden}
body{font-family:"Open Sans",Arial,sans-serif;color:var(--text);background:var(--white);position:relative}
h1,h2,h3,h4{font-family:"Montserrat",Arial,sans-serif}
section,header,footer{position:absolute;left:0;width:1200px}
.center{text-align:center}
.btn{display:inline-block;font-family:"Montserrat",sans-serif;font-weight:600;color:var(--white);text-decoration:none;font-size:17px;letter-spacing:.5px}

/* header */
.site-header{top:0;height:112px;background:var(--white)}
.brand{position:absolute;left:146px;top:34px;display:flex;align-items:center;gap:10px;font-family:"Montserrat",sans-serif;font-weight:700;font-size:30px;color:var(--dark)}
.brand i{width:30px;height:30px;border-radius:50%;background:var(--orange);display:block}
.nav{position:absolute;left:543px;top:46px;display:flex;gap:26px;font-size:15px;color:#444}
.nav a{color:#444;text-decoration:none}
.nav a.active{color:var(--green)}
.login{position:absolute;left:963px;top:37px;width:92px;height:38px;line-height:38px;text-align:center;background:var(--orange);font-size:14px}

/* hero */
.hero{top:112px;height:477px;background:linear-gradient(90deg,#6d6a66 0%,#8b8782 40%,#5b5b5b 100%)}
.hero-photo{position:absolute;inset:0;background:linear-gradient(90deg,rgba(90,80,70,.45),rgba(40,40,40,.55))}
.hero-content{position:absolute;left:0;right:0;top:170px;text-align:center;color:var(--white)}
.play{width:54px;height:54px;margin:0 auto}
.hero h1{font-size:44px;font-weight:600;margin-top:6px}
.hero p{font-size:14px;margin-top:10px;opacity:.9}
.hero .btn{margin-top:22px;background:var(--green);font-size:15px;padding:9px 20px}
.chev{position:absolute;top:222px;width:20px;height:30px}

/* integrations */
.integrations{top:589px;height:505px}
.integrations h3{position:absolute;top:42px;width:100%;text-align:center;color:var(--orange);font-size:23px;font-weight:600}
.apps{position:absolute;top:125px;left:160px;width:880px;display:flex;justify-content:space-between}
.app{width:150px;text-align:center}
.app span{display:block;width:48px;height:48px;margin:0 auto 12px;border-radius:8px}
.app b{font-family:"Open Sans",sans-serif;font-weight:600;font-size:18px;color:#555}
.integrations h4{position:absolute;top:290px;width:100%;text-align:center;font-size:20px;color:#222;font-weight:700}
.integrations p{position:absolute;top:333px;left:160px;width:880px;text-align:center;font-size:20px;line-height:30px;color:#555}
.integrations .btn{position:absolute;top:418px;left:510px;width:180px;height:46px;line-height:46px;text-align:center;background:var(--yellow)}

/* blue */
.features-band{top:1094px;height:454px;background:linear-gradient(180deg,#2aa5e6,#2497d6)}
.pillars{position:absolute;top:100px;left:180px;width:840px;display:flex;justify-content:space-between}
.pillar{width:200px;text-align:center;color:var(--white)}
.pillar svg{width:64px;height:64px}
.pillar h4{font-size:24px;font-weight:600;margin-top:14px}
.features-band p{position:absolute;top:314px;left:150px;width:900px;text-align:center;color:#eaf6fd;font-size:14px;line-height:24px}

/* dark */
.agencies{top:1548px;height:523px;background:linear-gradient(180deg,#3a3a3a,#4a4a4a)}
.agencies h2{position:absolute;top:96px;width:100%;text-align:center;color:var(--white);font-size:28px;font-weight:600}
.agencies p.lead{position:absolute;top:172px;left:150px;width:900px;text-align:center;color:#e8e8e8;font-size:14px;line-height:25px}
.agencies h4{position:absolute;top:308px;width:100%;text-align:center;color:var(--white);font-size:18px;font-weight:600}
.agencies small{position:absolute;top:356px;width:100%;text-align:center;color:#ccc;font-size:14px}
.agencies .btn{position:absolute;top:402px;left:491px;width:218px;height:56px;line-height:56px;text-align:center;background:var(--orange)}

/* green */
.organize{top:2071px;height:446px;background:var(--green-band)}
.organize h2{position:absolute;top:90px;width:100%;text-align:center;color:var(--white);font-size:28px;font-weight:600}
.organize p{position:absolute;left:130px;width:940px;text-align:center;color:#f1f9ea;font-size:14px;line-height:24px}

/* stress */
.stress{top:2517px;height:446px}
.stress h2{position:absolute;top:86px;width:100%;text-align:center;color:#333;font-size:28px;font-weight:600}
.stress p{position:absolute;top:152px;left:130px;width:940px;text-align:center;color:#888;font-size:14px;line-height:24px}
.stress .btn{position:absolute;top:347px;left:450px;width:300px;height:58px;line-height:58px;text-align:center;background:var(--blue)}

/* testimonial */
.testimonial{top:2963px;height:489px;background:linear-gradient(180deg,#1f1f1f,#3a3a3a)}
.testimonial h2{position:absolute;top:50px;width:100%;text-align:center;color:var(--white);font-size:30px;font-weight:600}
.avatar{position:absolute;top:128px;left:547px;width:106px;height:106px;border-radius:50%;border:4px solid var(--green-band);background:#8a8f95}
.testimonial blockquote{position:absolute;top:268px;left:150px;width:900px;text-align:center;color:#ddd;font-size:14px;line-height:24px}
.testimonial cite{position:absolute;top:378px;width:100%;text-align:center;color:var(--white);font-style:normal;font-weight:700;font-size:18px}
.testimonial .role{position:absolute;top:410px;width:100%;text-align:center;color:var(--green-band);font-size:17px}

/* cta */
.cta{top:3452px;height:164px;background:var(--orange)}
.cta h4{position:absolute;top:46px;width:100%;text-align:center;color:var(--white);font-size:17px;font-weight:600}
.cta .btn{position:absolute;top:90px;left:480px;width:240px;height:46px;line-height:44px;text-align:center;border:2px solid var(--white);font-size:14px}

/* contact */
.contact-bar{top:3616px;height:80px;background:var(--light)}
.contact-item{position:absolute;top:22px;display:flex;align-items:center;gap:10px;font-size:14px;color:#444}
.contact-item .ic{width:36px;height:36px;border-radius:50%;background:var(--blue);display:flex;align-items:center;justify-content:center}
.dots{display:flex;gap:6px;margin-left:4px}
.dots i{width:12px;height:12px;border-radius:50%;background:#555;display:block}

/* footer */
.site-footer{top:3696px;height:234px;background:var(--footer)}
.site-footer .brand{left:146px;top:60px;font-size:26px}
.col{position:absolute;top:34px;font-size:12px}
.col h5{font-family:"Montserrat",sans-serif;color:var(--blue);font-size:13px;font-weight:700;margin-bottom:14px}
.col ul{list-style:none;line-height:22px;color:#555}
.col li:before{content:"› ";color:var(--blue)}
.copyright{position:absolute;top:3930px;left:0;width:1200px;height:52px;background:var(--white);border-top:1px solid #e5e5e5;font-size:11px;color:#777}
.copyright .left{position:absolute;left:146px;top:19px}
.news{position:absolute;left:840px;top:12px;display:flex;align-items:center;gap:10px}
.news input{width:250px;height:26px;border:1px solid #ccc;font-size:11px;padding:0 8px}
.news b{background:var(--orange);color:var(--white);height:26px;line-height:26px;padding:0 12px;font-size:11px}
</style>
</head>
<body>

<header class="site-header">
  <div class="brand"><i></i>Korbalex</div>
  <nav class="nav"><a class="active" href="#">Home</a><a href="#">Features</a><a href="#">Pricing</a><a href="#">About Us</a><a href="#">Contact Us</a></nav>
  <a class="btn login" href="#">LOGIN</a>
</header>

<section class="hero">
  <div class="hero-photo" role="img" aria-label="Photo of a smiling professional working at a laptop in an office"></div>
  <svg class="chev" style="left:82px" viewBox="0 0 20 30"><path d="M15 4L5 15l10 11" stroke="#fff" stroke-width="3" fill="none"/></svg>
  <svg class="chev" style="left:1098px" viewBox="0 0 20 30"><path d="M5 4l10 11L5 26" stroke="#fff" stroke-width="3" fill="none"/></svg>
  <div class="hero-content">
    <svg class="play" viewBox="0 0 54 54"><circle cx="27" cy="27" r="24" stroke="#fff" stroke-width="3" fill="none"/><path d="M21 16l16 11-16 11z" fill="#fff"/></svg>
    <h1>Korbalex</h1>
    <p>Neque porro quisquam est qui dolorem ipsum quia dolor sit amet, consectetur, adipisci velit...</p>
    <a class="btn" href="#">GET STARTED NOW</a>
  </div>
</section>

<section class="integrations">
  <h3>Integrated with some of the most popular apps you already love.</h3>
  <div class="apps">
    <div class="app"><span style="background:#f4b400"></span><b>Stratafile</b></div>
    <div class="app"><span style="background:#f57c00"></span><b>Metrivue</b></div>
    <div class="app"><span style="background:#3d8de0"></span><b>Boxtern</b></div>
    <div class="app"><span style="background:#1e6e3a"></span><b>Ledgrove</b></div>
    <div class="app"><span style="background:#1976d2"></span><b>Cloudwick</b></div>
  </div>
  <h4>See what makes Korbalex a perfect tool!</h4>
  <p>See yourself the features that make Korbalex a perfect tool to manage your projects and get things done efficiently and in time.</p>
  <a class="btn" href="#">View Features</a>
</section>

<section class="features-band">
  <div class="pillars">
    <div class="pillar">
      <svg viewBox="0 0 64 64"><path d="M50 22A20 20 0 0 0 14 26" stroke="#fff" stroke-width="6" fill="none"/><path d="M54 12v14H40z" fill="#fff"/><path d="M14 42a20 20 0 0 0 36-4" stroke="#fff" stroke-width="6" fill="none"/><path d="M10 52V38h14z" fill="#fff"/></svg>
      <h4>Organize</h4>
    </div>
    <div class="pillar">
      <svg viewBox="0 0 64 64" fill="#fff"><circle cx="32" cy="18" r="9"/><path d="M16 50c0-12 7-18 16-18s16 6 16 18z"/><circle cx="13" cy="24" r="6"/><path d="M2 48c0-9 5-13 11-13 3 0 5 1 6 2-2 3-4 7-4 11z"/><circle cx="51" cy="24" r="6"/><path d="M62 48c0-9-5-13-11-13-3 0-5 1-6 2 2 3 4 7 4 11z"/></svg>
      <h4>Collaborate</h4>
    </div>
    <div class="pillar">
      <svg viewBox="0 0 64 64" fill="#fff"><rect x="8" y="22" width="48" height="12"/><rect x="12" y="36" width="40" height="22"/><rect x="29" y="22" width="6" height="36" fill="#2aa5e6"/><path d="M32 22c-6-10-16-10-14-3 1 3 8 3 14 3zM32 22c6-10 16-10 14-3-1 3-8 3-14 3z"/></svg>
      <h4>Deliver</h4>
    </div>
  </div>
  <p>Being an SEO agency we did not find any tool that can help agencies to manage an SEO project lifecycle effectively. That is why we decided to bring Korbalex "A robust SEO project management tool" for SEO Agencies to provide them the solution to manage their projects in an organized way.</p>
</section>

<section class="agencies" role="img" aria-label="Dark background photo of a desk with a laptop">
  <h2>Best Project Management Tool for Digital Agencies</h2>
  <p class="lead">Now SEO management is not at all a hectic task. Organize your SEO projects more effectively &amp; efficiently. Korbalex helps you to track every pitfall to projects and to find out their solutions on time. Give a powerful tool to your team to schedule their priorities &amp; finish things on time. Korbalex guides you to do the right things than to do things right. It is the most effective online tool that makes tasks easy and extremely manageable.</p>
  <h4>Make your projects more interesting and their solutions so constructive!</h4>
  <small>Features for Digital Agencies</small>
  <a class="btn" href="#">Start Your Free trail</a>
</section>

<section class="organize">
  <h2>Organize and Get it Done</h2>
  <p style="top:166px">Korbalex grants you access to measure every important aspect related to your projects effectively from a place. We believe what you measure you can manage. It's specifically designed for SEO project management keeping all project management needs in mind. You will get detailed information related to your projects online which will help you to get rid of offline management tools. It's armed with an effective dashboard that always provides updated project summary that helps you to evaluate the major important things and taking corrective actions on time.</p>
  <p style="top:316px">It's a most effective SEO management tool with major important features Like Time Management, Team Management, Task Management, Milestone Management, Mail Management and many more....</p>
</section>

<section class="stress">
  <h2>Stress! Take it out of your projects</h2>
  <p>Korbalex allows you to manage people, time and resources to properly implement an easy and stress free project management process. Using Korbalex, you can easily identify what could slow down your projects progress in future, and it enables you to take corrective actions in advance. Korbalex grants you access even to the minute detail of your projects, clients and team that helps you to manage things exceptionally well. Evaluation of tasks, workload, reports and manpower requirements is quite simple and fast to formulate strategies to meet the challenges. The detailed insight to your projects makes you feel confident while taking important decisions and dealing with your clients.</p>
  <a class="btn" href="#">Features for Digital Agencies</a>
</section>

<section class="testimonial">
  <h2>Still Not Convinced? See What They're Saying...</h2>
  <div class="avatar" role="img" aria-label="Portrait photo of the reviewer"></div>
  <svg class="chev" style="left:58px;top:222px" viewBox="0 0 20 30"><path d="M15 4L5 15l10 11" stroke="#fff" stroke-width="3" fill="none"/></svg>
  <svg class="chev" style="left:1122px;top:222px" viewBox="0 0 20 30"><path d="M5 4l10 11L5 26" stroke="#fff" stroke-width="3" fill="none"/></svg>
  <blockquote>" I have been handling SEO projects for the last 10 years. Korbalex SEO project management application is the first tool that is solely designed keeping in mind the needs of modern Search Engine Optimization. It has everything that SEO should have, features like Time Management, Milestone Management, Team Management, Mail Management etc. All these make it easy to manage your workforce and deliver above the client satisfaction. Can't Ask for More – Right! Thank you Korbalex and its fantastic team! "</blockquote>
  <cite>Tarek Velloni</cite>
  <div class="role">FreeLance</div>
</section>

<section class="cta">
  <h4>Share your experience with us and get 3 months of premium access for free</h4>
  <a class="btn" href="#">START 30 DAYS FREE TRAIL</a>
</section>

<section class="contact-bar">
  <div class="contact-item" style="left:140px"><span class="ic"><svg width="18" height="18" viewBox="0 0 24 24"><path d="M6 2l4 5-2 3c1 3 3 5 6 6l3-2 5 4-3 4C10 21 3 14 2 5z" fill="#fff"/></svg></span><b>Help &amp; Support</b>&nbsp;| +1-555-210-4837 FREE</div>
  <div class="contact-item" style="left:494px"><span class="ic"><svg width="18" height="18" viewBox="0 0 24 24"><rect x="2" y="5" width="20" height="14" fill="#fff"/><path d="M2 5l10 8 10-8" stroke="#2ea3e3" stroke-width="2" fill="none"/></svg></span><b>E-mail</b>&nbsp;: help@korbalex.com</div>
  <div class="contact-item" style="left:762px"><span class="ic"><svg width="18" height="18" viewBox="0 0 24 24"><circle cx="12" cy="12" r="8" stroke="#fff" stroke-width="3" fill="none"/></svg></span><b>Follow Us</b><span class="dots"><i></i><i></i><i></i></span></div>
</section>

<footer class="site-footer">
  <div class="brand"><i></i>Korbalex</div>
  <div class="col" style="left:300px"><h5>MENU</h5><ul><li>Home</li><li>Features</li><li>Pricing</li><li>About Us</li><li>Contact Us</li></ul></div>
  <div class="col" style="left:432px"><h5>FEATURES</h5><ul><li>Project Management</li><li>Constructive Dashboard</li><li>User-level Interface</li><li>Password Manager</li><li>Link Manager</li></ul></div>
  <div class="col" style="left:612px;top:66px"><ul><li>Client Management</li><li>Customize brand</li><li>Billing Management</li><li>Milestone Management</li></ul></div>
  <div class="col" style="left:772px;top:66px"><ul><li>Event Management</li><li>File manager</li><li>Task management</li></ul></div>
  <div class="col" style="left:944px"><h5>RESOURCES</h5><ul><li>Testimonials</li><li>3rd Party Apps</li><li>Support &amp; FAQs</li><li>Privacy Policy</li><li>Refund Policy</li></ul></div>
</footer>

<div class="copyright">
  <span class="left">© 2016, Korbalex by Nortavel Services Pvt. Ltd. All Rights Reserved.</span>
  <div class="news"><span>Newsletters</span><input type="text" placeholder="Enter Your E-mail Address"><b>SUBSCRIBE</b></div>
</div>

</body>
</html>
```